Medical equipment business looking for professional, unique business card

We need a business card design for a durable medical equipment company. We are small but would like our cards to express that we are much bigger. We focus on braces (back, knee, wrist, etc) but also do crutches, rollators, wheelchairs- basically medical equipment that gets you going and back in Action. Our colors are blue and green and our logo has an arrow and use of a "spine". We'd like to express professionalism while being unique.

Industry/Entity Type

Medical Equipment

Contact Information for Business Card

Professional feel but unique. Memorable.

Font styles to use
Serif
Sans Serif
Other font styles liked:
• verdana

Requirements
Must have
• card holders cell#, business phone#, fax#, email, website address, business address, logo
Nice to have
• use of medical/healthcare related descriptive words, items, look
Should not have
• the wrong colors or cartoon characters.

```html
<!DOCTYPE html>
<html lang="en">
<head>
<meta charset="UTF-8">
<title>Stride Care Supply – Business Card</title>
<link href="https://fonts.googleapis.com/css2?family=Roboto:wght@400;500&display=swap" rel="stylesheet">
<style>
  :root {
    --navy: #0d4470;
    --green: #8cc63f;
    --card: #f7f9fb;
    --backdrop: #dfe5ea;
    --ink: #14426a;
  }
  * { margin: 0; padding: 0; box-sizing: border-box; }
  html, body {
    width: 1200px; height: 900px; overflow: hidden;
    background: var(--backdrop);
    font-family: "Roboto", Verdana, sans-serif;
  }
  .business-card {
    position: absolute; left: 75px; top: 150px;
    width: 1050px; height: 600px;
    background: var(--card);
    border-radius: 22px;
    overflow: hidden;
    box-shadow: 0 10px 30px rgba(20, 50, 80, 0.18);
  }
  .side-wave { position: absolute; inset: 0; width: 1050px; height: 600px; }
  .brand-name {
    position: absolute; left: 74px; top: 112px;
    font-size: 56px; font-weight: 500; color: var(--navy);
    letter-spacing: -0.5px; line-height: 1;
  }
  .holder-name {
    position: absolute; left: 73px; top: 285px;
    font-size: 42px; font-weight: 500; color: var(--ink); line-height: 1;
  }
  .holder-role {
    position: absolute; left: 74px; top: 334px;
    font-size: 24px; font-weight: 400; color: var(--green); line-height: 1;
  }
  .contact-list {
    position: absolute; left: 74px; top: 378px;
    list-style: none;
  }
  .contact-item {
    display: flex; align-items: center; gap: 12px;
    height: 30px;
    font-size: 23px; color: var(--ink);
  }
  .contact-icon { width: 18px; height: 18px; fill: var(--green); flex: none; }
  .contact-address {
    position: absolute; left: 74px; top: 512px;
    font-size: 23px; font-weight: 500; color: var(--ink);
  }
</style>
</head>
<body>
  <div class="business-card">
    <svg class="side-wave" viewBox="0 0 1050 600" aria-hidden="true">
      <path fill="var(--green)" d="M676,0 C690,240 905,300 905,600 L1050,600 L1050,0 Z"/>
      <path fill="var(--navy)" d="M722,0 C700,220 968,320 936,600 L1050,600 L1050,0 Z"/>
    </svg>

    <div class="brand-name">Stride Care Supply</div>

    <h1 class="holder-name">Dale Morgan</h1>
    <p class="holder-role">Director Operations</p>

    <ul class="contact-list">
      <li class="contact-item">
        <svg class="contact-icon" viewBox="0 0 18 18"><path d="M4 1h10a2 2 0 0 1 2 2v12a2 2 0 0 1-2 2H4a2 2 0 0 1-2-2V3a2 2 0 0 1 2-2zm0 2v10h10V3z"/></svg>
        041-555-872
      </li>
      <li class="contact-item">
        <svg class="contact-icon" viewBox="0 0 18 18"><path d="M4 1l3 4-2 2c1 2.5 3.5 5 6 6l2-2 4 3-2 3C8 17 1 10 1 3z"/></svg>
        555-218-907
      </li>
      <li class="contact-item">
        <svg class="contact-icon" viewBox="0 0 18 18"><path d="M1 3h16v12H1zm2 2v1l6 4 6-4V5l-6 4z"/></svg>
        dale.morgan@stridecare.com
      </li>
      <li class="contact-item">
        <svg class="contact-icon" viewBox="0 0 18 18"><path d="M1 3h16v10H10v2h3v1H5v-1h3v-2H1zm2 2v6h12V5z"/></svg>
        www.stridecare-supply.com
      </li>
    </ul>

    <p class="contact-address">Linden Avenue, Denver 80211</p>
  </div>
</body>
</html>
```